political campaign lawn sign - Governor's Council in Massachuesetts

We are looking for a political lawn sign. We are running a campaign for Governor's Council in Massachusetts. This sign will be on the lawn of homes and businesses so people driving by will see it. It needs to be simple and bold. The last name is long so maybe it could say vote for Marty and then Kolbeck will be big a bold on the next line??
We need it to say:
Vote for Martin Kolbeck
Governor's Council.

Target Market(s)

local residents

Industry/Entity Type

Politcal Campaign

Font styles to use
Sans Serif
Other font styles liked:
• not sure what font but a modern looking one such as Helvetica, Arial, Sans Seri, sharp sans..

Colors
0054AA
0677BA
7BADD7
CADEEF
E8F1F8
00AB8E
00BBA5
67D7C9
C6EFE9
E9F9F6
FFF300
FFF600
FEFA6F
FFFEC7
FFFEE8

Requirements
Must have
• My name written out with a Capital D and R but lower case for every other letter so its Marty Kolbeck
Nice to have
• modern font , the Colors of the lawn sign should have Blue, Yellow and White something bold that will stand out
Should not have
• any maps of Massachusetts

```html
<!DOCTYPE html>
<html lang="en">
<head>
<meta charset="utf-8">
<title>Vote For Martin Kolbeck – Governor's Council</title>
<link rel="stylesheet" href="https://fonts.googleapis.com/css2?family=Fira+Sans:wght@600;700&display=swap">
<style>
  :root {
    --campaign-blue: #0054AA;
    --name-white: #E8F1F8;
    --band-cream: #FFFEE8;
    --shadow: rgba(0, 20, 60, 0.45);
  }
  html, body {
    margin: 0;
    padding: 0;
    width: 1129px;
    height: 1200px;
    overflow: hidden;
    background: #ffffff;
  }
  .lawn-sign {
    width: 1129px;
    height: 1200px;
    display: flex;
    flex-direction: column;
    font-family: "Fira Sans", Arial, sans-serif;
  }
  .sign-headline {
    flex: 0 0 780px;
    background: var(--campaign-blue);
    color: var(--name-white);
    display: flex;
    flex-direction: column;
    align-items: center;
    justify-content: center;
    text-align: center;
  }
  .vote-for {
    font-weight: 600;
    font-size: 104px;
    line-height: 1;
    margin: 0 0 20px;
    text-shadow: 3px 4px 6px var(--shadow);
  }
  .candidate-name {
    font-weight: 600;
    font-size: 142px;
    line-height: 1;
    margin: 0;
    white-space: nowrap;
    letter-spacing: 0.5px;
    text-shadow: 4px 6px 8px var(--shadow);
  }
  .sign-office {
    flex: 1 1 auto;
    background: var(--band-cream);
    color: var(--campaign-blue);
    display: flex;
    align-items: center;
    justify-content: center;
  }
  .office-title {
    font-weight: 700;
    font-size: 100px;
    line-height: 1;
    margin: 0;
    white-space: nowrap;
  }
</style>
</head>
<body>
  <main class="lawn-sign">
    <section class="sign-headline">
      <p class="vote-for">Vote For</p>
      <h1 class="candidate-name">Martin Kolbeck</h1>
    </section>
    <section class="sign-office">
      <p class="office-title">Governor's Council.</p>
    </section>
  </main>
</body>
</html>
```